Homes, Invest in Non-performing loans

We need only 3 web pages, one for the home, one for the content, one for the properties.
The main focus of our business is to offer non performing loans (before foreclosures) to the general public. All the non-performing mortgages will end in a house, an apartment, a store, etc.
Our customers are able to invest from 10,000usd to 1,000,000usd (average 50,000usd).
Our customers' usual focus groups are employees who want second earnings, perceiving the business feeling without outlay time. They look for a solid finance sense corporation that confers them certainty.
Nearly all our clients desire the house, apartment, store, etc. more than the actual earnings.
The name of our company is BRAMLEX
Reason: We value the time and effort you already invest in our project. We realize that we did't come back on some of the doubts requested by the designers. It will be inequitable to the designers who prerequisite our feedback. We also appreciate the comprehension of the community in this postponement.
Reason: Designers,
We really apreciate all the time and effort you put on our project. From the begining we ask for 3 pages, so now we will leave the 10 finalist and provide some extra time to submit the other 2 pages.
We will race the price in 10%
Target Market(s)
Our customers average investors works as employees and want to have a second income or business without spending time. (People from 35 to 50)
Industry/Entity Type
Finance
Requirements
Should not have
- FLASH

```html
<!DOCTYPE html>
<html lang="es">
<head>
<meta charset="utf-8">
<title>BRAMLEX · Remates</title>
<link href="https://fonts.googleapis.com/css2?family=Cabin:wght@400;500&display=swap" rel="stylesheet">
<style>
:root{
  --green:#7b8a14;
  --green-dark:#6a7a10;
  --text:#8c9191;
  --text-strong:#7c8282;
  --nav:#6f7575;
  --band-top:#e4e8e6;
  --band-bottom:#f3f5f4;
  --rule:#cfd8d6;
  --footer:#e3e7e5;
  --white:#ffffff;
}
*{margin:0;padding:0;box-sizing:border-box}
html,body{width:1200px;height:1158px;overflow:hidden;background:var(--white);font-family:"Cabin",sans-serif}
.page{position:relative;width:1200px;height:1158px}
.header-band{position:absolute;left:0;top:0;width:1200px;height:118px;background:linear-gradient(180deg,var(--band-top),var(--band-bottom));border-bottom:1px solid #dde2e0}
.brand-box{position:absolute;left:114px;top:0;width:224px;height:158px;background:linear-gradient(180deg,#f6f7f7,#fff 60%);border:1px solid #d8dcdb;box-shadow:0 2px 4px rgba(0,0,0,.12);text-align:center}
.brand-name{position:absolute;left:0;right:0;top:78px;font-size:30px;font-weight:500;color:var(--green-dark);letter-spacing:1px}
.brand-mark{position:absolute;left:100px;top:40px;width:24px;height:24px;background:var(--green)}
.brand-tag{position:absolute;left:0;right:0;top:123px;font-size:8px;letter-spacing:1.2px;color:#333}
.join{position:absolute;left:879px;top:12px;font-size:14px;color:#333}
.social{position:absolute;top:13px;width:16px;height:16px;border-radius:50%;background:var(--green)}
.social-sep{position:absolute;left:1033px;top:0;width:1px;height:46px;background:#d3d8d6}
.nav a{position:absolute;top:88px;font-size:15px;color:var(--nav);text-decoration:none}
.nav .active-tab{position:absolute;left:430px;top:70px;width:112px;height:48px;background:linear-gradient(180deg,rgba(255,255,255,0),#f7f8f8)}
.nav .active{color:var(--green)}
.nav-sep{position:absolute;left:710px;top:80px;width:1px;height:32px;background:#d3d8d6}
.subnav a{position:absolute;top:131px;font-size:13px;color:var(--green-dark);text-decoration:none}
.subnav-rule{position:absolute;left:340px;top:156px;width:470px;height:2px;background:linear-gradient(90deg,#e9ecec,rgba(233,236,236,0))}
.contact{position:absolute;left:130px;top:260px}
.contact svg{position:absolute;left:0;top:0}
.contact h3{position:absolute;left:28px;top:1px;font-size:15px;font-weight:400;color:var(--green);white-space:nowrap}
.contact p{position:absolute;left:29px;font-size:12px;color:#4e5454;white-space:nowrap}
.listing{position:absolute;left:370px;width:688px}
.listing h2{position:absolute;left:0;top:0;font-size:22px;font-weight:400;color:var(--green)}
.listing .desc{position:absolute;left:0;top:40px;width:488px;font-size:12px;line-height:17px;color:var(--text)}
.listing .prices{position:absolute;left:0;font-size:17px;line-height:22px;color:var(--text-strong)}
.prices span{display:inline-block;width:103px}
.photo{position:absolute;left:508px;top:42px;width:180px;height:128px;border:1px solid #9aa2a2;border-radius:3px}
.rule{position:absolute;left:368px;width:689px;height:1px;background:var(--rule)}
.footer{position:absolute;left:330px;top:1126px;width:594px;height:32px;background:var(--footer);font-size:11px;color:#555;padding:9px 0 0 12px}
</style>
</head>
<body>
<div class="page">
  <div class="header-band"></div>

  <div class="brand-box">
    <div class="brand-mark"></div>
    <div class="brand-name">BRAMLEX</div>
    <div class="brand-tag">REMATES HIPOTECARIOS</div>
  </div>

  <div class="join">Únete a nosotros</div>
  <div class="social" style="left:1008px"></div>
  <div class="social-sep"></div>
  <div class="social" style="left:1042px"></div>

  <nav class="nav">
    <div class="active-tab"></div>
    <a style="left:370px">Home</a>
    <a class="active" style="left:457px">Remates</a>
    <a style="left:572px">Quienes Somos</a>
    <div class="nav-sep"></div>
    <a style="left:738px">Contacto</a>
  </nav>

  <nav class="subnav">
    <a style="left:369px">Interes social</a>
    <a style="left:460px">Medio</a>
    <a style="left:511px">Residencial</a>
    <a style="left:588px">Alto</a>
    <a style="left:625px">En el Pais</a>
    <a style="left:692px">Negocios</a>
  </nav>
  <div class="subnav-rule"></div>

  <aside class="contact">
    <svg width="22" height="22" viewBox="0 0 22 22"><circle cx="11" cy="11" r="9.5" fill="none" stroke="#7b8a14" stroke-width="1.6"/><path d="M8 6.5c-1 .6-1.3 2-.4 3.8 1 1.9 2.5 3.5 4.3 4.5 1.6.9 2.8.6 3.4-.3l-1.7-1.6-1.2.7c-1-.5-2-1.6-2.5-2.7l.8-1.1z" fill="#7b8a14"/></svg>
    <h3>Contacto</h3>
    <p style="top:20px">ventas@bramlex.mx</p>
    <p style="top:38px">SALES (55) 4100-3700</p>
  </aside>

  <section class="listing" style="top:180px">
    <h2>Interes social</h2>
    <p class="desc">Son principalmente, casas habitación e inmuebles con superficies que van de los 50 m²&nbsp; a los 80m² y cuentan con 2 recámaras, sala, comedor, cocina y 1 lugar de estacionamiento. Están muy bien ubicados tanto en el Estado de México, (Tultitlán, Ecatepec, Cuautitlán, etc.) como en el Distrito Federal (Azcapotzalco, Iztapalapa, etc.)</p>
    <div class="prices" style="top:140px"><span>Valor bramlex</span>:&nbsp; De $100,000 hasta $ 350,000<br><span>Valor real</span>:&nbsp; De $350,000 hasta $ 700,000</div>
    <div class="photo" role="img" aria-label="Casa de interés social de dos niveles con ventanas rojas" style="top:56px;background:linear-gradient(180deg,#e9ece8 0%,#efe6e0 70%,#7fb04a 100%)"></div>
  </section>
  <div class="rule" style="top:390px"></div>

  <section class="listing" style="top:410px">
    <h2>Interes Medio</h2>
    <p class="desc" style="top:55px">Son departamentos de 80m² que cuentan con 3 recámaras, sala, comedor, cocina, 1 lugar de estacionamiento. Muy bien ubicado, en el Estado de México: Toluca, Cuautitlán, Atizapán, Naucalpan. En el Distrito Federal (Coyoacán, Benito Juárez, Miguel Hidalgo).</p>
    <div class="prices" style="top:140px"><span>Valor bramlex</span>:&nbsp; De $500,000 hasta $ 900,000<br><span>Valor real</span>:&nbsp; De $700,000 hasta $ 2,000,000</div>
    <div class="photo" role="img" aria-label="Fachada de departamentos con techo de teja y jardín" style="top:57px;background:linear-gradient(180deg,#f0ebd8 0%,#e8e2cf 55%,#c8603a 62%,#eee9da 75%,#6fa53c 100%)"></div>
  </section>
  <div class="rule" style="top:620px"></div>

  <section class="listing" style="top:640px">
    <h2>Residencial</h2>
    <p class="desc" style="top:55px">Tenemos casas solas y condominio horizontal o departamentos amplios con 120m² o más, que cuentan con 3 recamaras, 2 baños, sala comedor, cocina y estacionamiento. Están ubicados en zonas comerciales como Del Valle, Condesa, Las Águilas, Lindavista, Coyoacán, Cuajimalpa, Satélite, Naucalpan</p>
    <div class="prices" style="top:140px"><span>Valor bramlex</span>:&nbsp; De $1,000,000 hasta $ 2,000,000<br><span>Valor real</span>:&nbsp; De $1,800,000 hasta $ 3,500,000</div>
    <div class="photo" role="img" aria-label="Casa residencial moderna con balcón de vidrio" style="top:57px;background:linear-gradient(135deg,#e4ecee 0%,#bfd3d6 45%,#4b5a5a 70%,#cfd9d6 100%)"></div>
  </section>
  <div class="rule" style="top:854px"></div>

  <section class="listing" style="top:874px">
    <h2>Alto</h2>
    <p class="desc" style="top:55px">Casas de lujo ubicadas en zonas como Huixquilucan, Satélite, Coyoacán, Álvaro Obregón. Tienen más de 300m² de terreno y de construcción; 3 o 4 recamaras, sala, comedor, cocina, 2 o 3 estacionamientos, estudio, estancia.</p>
    <div class="prices" style="top:123px"><span>Valor bramlex</span>:&nbsp; De $2,000,000 en aldente<br><span>Valor real</span>:&nbsp; De $3,500,000 en aldente</div>
    <div class="photo" role="img" aria-label="Residencia de lujo moderna con alberca" style="top:57px;background:linear-gradient(180deg,#eef1f2 0%,#d6dadb 35%,#3c4444 55%,#f2f2f0 75%,#6cc3e0 100%)"></div>
  </section>

  <footer class="footer">© 2013 BRAMLEX . All rights reserved.</footer>
</div>
</body>
</html>
```